Bar Soap Packaging Design for Facial Cleansing Bar

Hi,

I have a business that sells soaps, lotions, and other skincare products and I'd like a design for a box for a bar soap that is primarily for women.

The name of the brand is 'Velmo Shea Blend' and the brand is all about renewal and rejuvenation.

I've attached my logo and photos of packaging for bar soaps that are best sellers in my market.

The box is 3 inches x 2 inches and has a white background.

Info to go on the box:

1. Brand name: Velmo Shea Blend

2. [To go below brand name]: Facial Bar

3. Address: Distributed by Haverlin Trading Ltd, 47 Marlow St., Kingston, Jamaica W.I.

4. Contact: tamsin@velmosheablend.example

5. Net Weight: 3.6 oz /102g

6. Ingredients: glycerine, palmitic acid, sodium chloride, water, Shea Blend, fragrance, AOS, EDTA, vitamin E, color.

7. Directions: Wet face. Lather soap in hands. Gently massage lather onto face and neck. Rinse with water and pat dry with a towel. For day, follow with a sunscreen. At night, follow with a serum and/or moisturizer.

8. Please put a circle somewhere on the front with the words: 'Boosts Hydration 100%' in the circle

9. Batch Code: [please leave space beside 'Batch Code' blank]

10. Best Before: April 2019

11. Please put somewhere on the the front: For Younger Looking Skin

12. Please put somewhere on the front: with Real Shea Blend and Vitamin E

Thank you,
Tamsin

Target Market(s)

Women 27 to 60 who are looking for anti-age skincare products that'll make them look younger

Industry/Entity Type

Business

Font styles to use
Sans Serif

Colors

Designer to choose colors to be used in the design.

Requirements
Must have
• The info that I've asked for in the brief
Nice to have
• A design similar to the packaging for the brand of soap 'Odra' that I've attached.
Should not have
• Not sure...

```html
<!DOCTYPE html>
<html lang="en">
<head>
<meta charset="utf-8">
<title>Velmo Shea Blend – Facial Bar Box Front</title>
<link rel="stylesheet" href="https://fonts.googleapis.com/css2?family=Marcellus&family=Questrial&family=Montserrat:wght@500;700&display=swap">
<style>
  :root {
    --backdrop: #e6e7e8;
    --panel: #f7f7f9;
    --brand-violet: #3d3b98;
    --deep-red: #9b1c2a;
    --rose: #d9627e;
    --rose-band: #e27b96;
    --ribbon-red: #d2182c;
    --ribbon-dark: #2a1418;
    --ribbon-pink: #f0a3b4;
  }
  * { margin: 0; padding: 0; box-sizing: border-box; }
  html, body { width: 1200px; height: 857px; overflow: hidden; }
  body { background: var(--backdrop); position: relative; }

  .box-front {
    position: absolute; left: 160px; top: 128px;
    width: 880px; height: 600px;
    background: linear-gradient(135deg, #ffffff 0%, var(--panel) 55%, #eceef2 100%);
    overflow: hidden;
  }
  .ribbon-art { position: absolute; inset: 0; }

  .brand-name {
    position: absolute; left: 28px; top: 34px;
    font-family: "Marcellus", serif; font-size: 124px; line-height: 1;
    color: var(--brand-violet);
  }
  .product-line {
    position: absolute; left: 44px; top: 214px;
    font-family: "Marcellus", serif; font-size: 46px; letter-spacing: 1px; line-height: 1;
    color: var(--deep-red);
  }

  .ingredient-tag {
    position: absolute; left: 454px; top: 70px; width: 408px; height: 82px;
  }
  .ingredient-tag .pill {
    position: absolute; left: 72px; top: 15px; right: 0; height: 54px;
    border: 2px solid var(--deep-red); border-radius: 10px;
    background: rgba(255,255,255,.88);
    padding: 2px 14px 0 0; text-align: right;
    font-family: "Questrial", sans-serif; font-size: 21px; line-height: 24px;
    color: var(--deep-red);
  }
  .ingredient-tag .dot {
    position: absolute; left: 0; top: 0; width: 82px; height: 82px; z-index: 1;
    border-radius: 50%; border: 3px solid var(--deep-red); background: #fff;
  }
  .ingredient-tag .dot::after {
    content: ""; position: absolute; inset: 14px;
    border-radius: 50%; background: var(--deep-red); opacity: .85;
  }

  .facial-bar {
    position: absolute; left: 41px; top: 408px;
    font-family: "Questrial", sans-serif; font-size: 58px; line-height: 1;
    color: var(--rose);
  }
  .facial-bar strong { font-family: "Montserrat", sans-serif; font-weight: 700; }

  .claim-band {
    position: absolute; left: 44px; top: 494px; width: 606px; height: 44px;
    background: var(--rose-band);
    font-family: "Montserrat", sans-serif; font-weight: 700; font-size: 25px;
    font-variant: small-caps; letter-spacing: 1.5px; line-height: 44px;
    color: #fff; padding-left: 14px;
  }

  .hydration-seal { position: absolute; left: 656px; top: 390px; width: 176px; height: 176px; }
</style>
</head>
<body>
  <main class="box-front">
    <svg class="ribbon-art" width="880" height="600" viewBox="0 0 880 600" role="img" aria-label="Flowing red, pink and black abstract ribbon artwork sweeping across the right side">
      <defs>
        <linearGradient id="ribbonFill" x1="1" y1="0" x2="0" y2="1">
          <stop offset="0" stop-color="var(--ribbon-dark)"/>
          <stop offset=".3" stop-color="var(--ribbon-red)"/>
          <stop offset=".65" stop-color="var(--ribbon-pink)"/>
          <stop offset="1" stop-color="#ffffff" stop-opacity="0"/>
        </linearGradient>
      </defs>
      <path d="M760 0 L880 0 L880 600 L360 600 C520 520 650 300 760 0 Z" fill="url(#ribbonFill)"/>
    </svg>

    <h1 class="brand-name">Velmo</h1>
    <p class="product-line">SHEA BLEND</p>

    <div class="ingredient-tag">
      <span class="dot"></span>
      <p class="pill">with Real Shea Blend<br>and Vitamin E</p>
    </div>

    <p class="facial-bar">Facial<strong>Bar</strong></p>
    <p class="claim-band">For Younger Looking Skin</p>

    <svg class="hydration-seal" viewBox="0 0 180 180" aria-label="Boosts Hydration 100%">
      <defs>
        <path id="sealArc" d="M32 96 A58 58 0 0 1 148 96"/>
      </defs>
      <circle cx="90" cy="90" r="84" fill="rgba(255,255,255,.8)" stroke="var(--rose)" stroke-width="4"/>
      <circle cx="90" cy="90" r="74" fill="none" stroke="var(--rose)" stroke-width="2"/>
      <text font-family="Questrial, sans-serif" font-size="21" fill="var(--rose)" letter-spacing="1">
        <textPath href="#sealArc" startOffset="50%" text-anchor="middle">Boosts Hydration</textPath>
      </text>
      <path d="M90 64 L108 100 A20 20 0 0 1 72 100 Z" fill="none" stroke="var(--rose)" stroke-width="4" stroke-linejoin="round"/>
      <text x="90" y="142" text-anchor="middle" font-family="Montserrat, sans-serif" font-weight="700" font-size="32" fill="#fff" stroke="var(--rose)" stroke-width="1.5">100%</text>
    </svg>
  </main>
</body>
</html>
```